Cosmetic injections clinic needs a fresh looking business card

We need a business card using the supplied logo and color scheme to attract future clients to our clinic. It should be modern and fresh, eye catching and not too busy. Simple and to the point is best. I would like two sided designs with the front indicating address and contact information, and the back in full color with white logo and descriptive information also provided.
Target Market(s)
Clients looking for non surgical beauty enhancements.
Contact Information for Business Card
MeloraSkin
14, 618 Birchmont Way
St. Albert, Alberta
K2P 7W3
Phone: 587-412-6630
Email: info@meloraskin.com
Requirements
Must have
- -Logo supplied with the name and address of the clinic
- -Back of card in full color with white logo with A small line of text indicating both of the following: Anti aging consultants and cosmetic injectables
- Located inside the Voyager Wellness Group

```html
<!DOCTYPE html>
<html lang="en">
<head>
<meta charset="utf-8">
<title>MeloraSkin Business Card – Front and Back</title>
<link href="https://fonts.googleapis.com/css2?family=Arimo:wght@400;700&family=Source+Sans+3:wght@400&family=Tinos&display=swap" rel="stylesheet">
<style>
  :root {
    --paper: #ffffff;
    --ink: #111111;
    --navy: #0e4a5a;
    --teal: #33b7a1;
    --pink: #e2479b;
    --purple: #8a6bb4;
    --logo-purple: #7b4fa8;
    --mark: #9a9a9a;
    --border: #333333;
  }
  * { margin: 0; padding: 0; box-sizing: border-box; }
  html, body { width: 1200px; height: 1200px; overflow: hidden; background: var(--paper); }
  .sheet { position: relative; width: 1200px; height: 1200px; }

  .side-label {
    position: absolute; top: 300px; width: 443px; text-align: center;
    font-family: "Tinos", serif; font-size: 40px; color: var(--ink);
  }
  .side-label--front { left: 122px; }
  .side-label--back { left: 614px; }

  .crop-marks { position: absolute; inset: 0; }

  .card {
    position: absolute; top: 402px; width: 444px; height: 251px;
    border: 1px solid var(--border); overflow: hidden;
  }
  .card--front { left: 121px; background: var(--paper); }
  .card--back { left: 614px; background: var(--teal); }

  .front-art { position: absolute; inset: 0; }

  .brand-lockup {
    position: absolute; display: flex; align-items: center; gap: 5px;
    font-family: "Arimo", sans-serif; font-weight: 400; white-space: nowrap;
  }
  .brand-lockup__dot { border-radius: 50%; flex: none; }
  .card--front .brand-lockup { left: 17px; top: 52px; }
  .card--front .brand-lockup__dot { width: 20px; height: 20px; background: var(--logo-purple); }
  .card--front .brand-lockup__name { font-size: 16px; color: var(--logo-purple); }

  .contact {
    position: absolute; left: 22px; top: 109px;
    font-family: "Arimo", sans-serif; color: var(--ink); white-space: nowrap;
  }
  .contact__name { font-size: 19px; font-weight: 700; margin-bottom: 7px; }
  .contact__line { font-size: 16px; line-height: 20px; }

  .card--back .brand-lockup {
    left: 0; right: 0; top: 78px; justify-content: center; gap: 12px;
  }
  .card--back .brand-lockup__dot { width: 70px; height: 70px; background: var(--paper); }
  .card--back .brand-lockup__name { font-size: 42px; color: var(--paper); }

  .tagline {
    position: absolute; left: 0; right: 0; top: 198px; text-align: center;
    font-family: "Source Sans 3", sans-serif; font-size: 10.5px; color: var(--paper);
  }
</style>
</head>
<body>
<div class="sheet">
  <div class="side-label side-label--front">front</div>
  <div class="side-label side-label--back">back</div>

  <svg class="crop-marks" width="1200" height="1200" viewBox="0 0 1200 1200" aria-hidden="true">
    <g stroke="var(--mark)" stroke-width="1">
      <line x1="121.5" y1="326" x2="121.5" y2="376"/>
      <line x1="565.5" y1="326" x2="565.5" y2="376"/>
      <line x1="614.5" y1="326" x2="614.5" y2="376"/>
      <line x1="1058.5" y1="326" x2="1058.5" y2="376"/>
      <line x1="121.5" y1="678" x2="121.5" y2="726"/>
      <line x1="565.5" y1="678" x2="565.5" y2="726"/>
      <line x1="614.5" y1="678" x2="614.5" y2="726"/>
      <line x1="1058.5" y1="678" x2="1058.5" y2="726"/>
      <line x1="72" y1="401.5" x2="96" y2="401.5"/>
      <line x1="72" y1="653.5" x2="96" y2="653.5"/>
      <line x1="1083" y1="401.5" x2="1112" y2="401.5"/>
      <line x1="1083" y1="653.5" x2="1112" y2="653.5"/>
      <line x1="565" y1="653.5" x2="614" y2="653.5"/>
    </g>
  </svg>

  <section class="card card--front">
    <svg class="front-art" width="444" height="251" viewBox="0 0 444 251">
      <defs>
        <linearGradient id="pattern-tones" x1="0" y1="0" x2="1" y2="1">
          <stop offset="0" stop-color="var(--pink)"/>
          <stop offset="0.45" stop-color="var(--purple)"/>
          <stop offset="0.75" stop-color="var(--teal)"/>
          <stop offset="1" stop-color="var(--pink)"/>
        </linearGradient>
      </defs>
      <path role="img" aria-label="Colourful mandala pattern in pink, purple and teal"
            d="M0,4 C70,0 135,16 165,66 C190,108 218,172 258,204 C293,230 362,251 444,251 L444,0 L0,0 Z"
            fill="url(#pattern-tones)"/>
      <path d="M0,8 C70,4 130,20 160,70 C185,112 215,175 255,206 C290,232 360,250 444,250"
            fill="none" stroke="var(--navy)" stroke-width="7"/>
    </svg>

    <div class="brand-lockup">
      <span class="brand-lockup__dot"></span>
      <span class="brand-lockup__name">MeloraSkin</span>
    </div>

    <div class="contact">
      <p class="contact__name">MeloraSkin</p>
      <p class="contact__line">14, 618 Birchmont Way</p>
      <p class="contact__line">St. Albert, Alberta</p>
      <p class="contact__line">K2P 7W3</p>
      <p class="contact__line">Phone: 587-412-6630</p>
      <p class="contact__line">Email: info@meloraskin.com</p>
    </div>
  </section>

  <section class="card card--back">
    <div class="brand-lockup">
      <span class="brand-lockup__dot"></span>
      <span class="brand-lockup__name">MeloraSkin</span>
    </div>
    <p class="tagline">Anti aging consultants and cosmetic injectables</p>
  </section>
</div>
</body>
</html>
```